Business Book - Quiet Mornings at the Ledger Desk (Finding Calm Among Daily Numbers)

I'm looking for a cover that appeals to successful business people who are used to reading business titles.

The cover should feel familiar and fit in with the existing canon of bestselling business books with a vibrant, but professional look (see attached).

I want my book to stand out, but not to be frivolous. Abstract is probably best. Or close to it.

Please feel free to use my brand colours, or go with something else -

Teal
HEX #199BAB
25 / 155 / 171

Coral
HEX #EE786E
238 / 120/ 110

I don't want to include anything connected with robots or gendered assistants/business people. Or headsets.

It's only 24 hours which is mental

```html
<!DOCTYPE html>
<html lang="en">
<head>
<meta charset="utf-8">
<title>Quiet Mornings at the Ledger Desk — Book Cover</title>
<link href="https://fonts.googleapis.com/css2?family=Anton&family=Lato:wght@400&family=Montserrat:wght@800&family=Oswald:wght@700&display=swap" rel="stylesheet">
<style>
  :root {
    --paper: #ffffff;
    --coral: #ea756b;
    --coral-soft: #f3b3ab;
    --teal-soft: #a9dbe1;
    --ink: #141414;
    --title-dark: #333333;
    --title-light: #ffffff;
    --gold-deep: #d9a941;
    --gold-pale: #f3e68f;
    --gold-mid: #e3cb6d;
    --gold-dark: #c4922f;
  }
  html, body {
    margin: 0;
    padding: 0;
    width: 748px;
    height: 1200px;
    overflow: hidden;
    background: var(--paper);
  }
  .cover {
    position: relative;
    width: 748px;
    height: 1200px;
    background: var(--paper);
  }
  .cover svg { display: block; }
  .author-name {
    font-family: "Lato", "Gill Sans", sans-serif;
    font-weight: 400;
    fill: var(--ink);
  }
  .title-lead {
    font-family: "Oswald", "Arial Narrow", sans-serif;
    font-weight: 700;
    fill: var(--title-dark);
  }
  .title-main {
    font-family: "Anton", "Impact", sans-serif;
    fill: var(--title-light);
  }
  .subtitle {
    font-family: "Montserrat", "Futura", sans-serif;
    font-weight: 800;
    fill: url(#goldFoil);
  }
  .subtitle-rule {
    stroke: url(#goldFoil);
    stroke-width: 1.5;
  }
</style>
</head>
<body>
<main class="cover">
  <svg width="748" height="1200" viewBox="0 0 748 1200" xmlns="http://www.w3.org/2000/svg">
    <defs>
      <linearGradient id="halftoneTone" x1="0" y1="0" x2="1" y2="1">
        <stop offset="0" stop-color="var(--teal-soft)" stop-opacity="0.55"/>
        <stop offset="0.5" stop-color="var(--coral-soft)" stop-opacity="0.45"/>
        <stop offset="1" stop-color="var(--teal-soft)" stop-opacity="0.5"/>
      </linearGradient>
      <linearGradient id="goldFoil" x1="0" y1="0" x2="1" y2="0">
        <stop offset="0" stop-color="var(--gold-deep)"/>
        <stop offset="0.3" stop-color="var(--gold-pale)"/>
        <stop offset="0.55" stop-color="var(--gold-mid)"/>
        <stop offset="0.8" stop-color="var(--gold-dark)"/>
        <stop offset="1" stop-color="var(--gold-mid)"/>
      </linearGradient>
    </defs>

    <g class="halftone-field" role="img" aria-label="Decorative field of small teal and coral dots">
      <path d="M0 0 H290 L330 60 L400 140 L450 200 L470 240 L460 300 L400 380 L300 460 L230 560 L200 700 L190 800 L150 860 L110 900 L60 920 L0 920 Z" fill="url(#halftoneTone)"/>
      <path d="M660 520 L700 540 L748 560 V780 L660 780 L620 760 Z" fill="url(#halftoneTone)"/>
    </g>

    <circle class="title-disc" cx="387" cy="540" r="307" fill="var(--coral)"/>

    <text class="author-name" x="376" y="129" font-size="56" text-anchor="middle" textLength="512" lengthAdjust="spacingAndGlyphs">MAREN HOLLOWAY</text>

    <text class="title-lead" x="391" y="418" font-size="62" text-anchor="middle" textLength="450" lengthAdjust="spacingAndGlyphs">Quiet Mornings At The</text>
    <text class="title-main" x="391" y="576" font-size="160" text-anchor="middle" textLength="420" lengthAdjust="spacingAndGlyphs">Ledger</text>
    <text class="title-main" x="391" y="724" font-size="118" text-anchor="middle">Desk</text>

    <text class="subtitle" x="374" y="1003" font-size="46" text-anchor="middle" textLength="583" lengthAdjust="spacingAndGlyphs">FINDING CALM AMONG</text>
    <line class="subtitle-rule" x1="50" y1="1035" x2="263" y2="1035"/>
    <text class="subtitle" x="374" y="1053" font-size="44" text-anchor="middle">DAILY</text>
    <line class="subtitle-rule" x1="518" y1="1035" x2="730" y2="1035"/>
    <text class="subtitle" x="384" y="1149" font-size="116" text-anchor="middle" textLength="669" lengthAdjust="spacingAndGlyphs">NUMBERS</text>
  </svg>
</main>
</body>
</html>
```